Business Card for a New Zealand IT Startup

I need a business card for Talmor Ventures. We are a young startup based in New Zealand working in internet marketing and web development. The design should have some element connected to New Zealand, such as wave, koru or silver fern, just don't use a kiwi bird.

```html
<!DOCTYPE html>
<html lang="en">
<head>
<meta charset="utf-8">
<title>Talmor Ventures – Business Card</title>
<link href="https://fonts.googleapis.com/css2?family=Poppins:wght@300;400;600&display=swap" rel="stylesheet">
<style>
  :root {
    --bg: #eef0f2;
    --card: #ffffff;
    --orange: #f15a24;
    --blue: #0a6cb8;
    --ink: #1d1d1d;
    --on-orange: #ffffff;
  }
  html, body {
    margin: 0;
    width: 1200px;
    height: 1200px;
    overflow: hidden;
    background: var(--bg);
    font-family: "Poppins", sans-serif;
  }
  .canvas {
    position: relative;
    width: 1200px;
    height: 1200px;
  }
  .card {
    position: absolute;
    left: 180px;
    width: 840px;
    height: 480px;
    box-shadow: 0 10px 26px rgba(0,0,0,0.12);
    overflow: hidden;
    background: var(--card);
  }
  .card-back { top: 90px; }
  .card-front { top: 630px; }
  .card svg { display: block; }
  .brand-name {
    font-family: "Poppins", sans-serif;
    font-weight: 600;
    fill: var(--blue);
  }
  .service {
    font-family: "Poppins", sans-serif;
    font-weight: 300;
    font-size: 30px;
    fill: var(--ink);
  }
  .contact {
    font-family: "Poppins", sans-serif;
    font-weight: 300;
    font-size: 20px;
    fill: var(--on-orange);
  }
  .icon-tab { fill: var(--blue); }
  .icon-glyph { fill: none; stroke: #fff; stroke-width: 2; }
  .icon-fill { fill: #fff; }
</style>
</head>
<body>
<main class="canvas">

  <!-- Back side: services and contact details -->
  <section class="card card-back" aria-label="Business card back">
    <svg width="840" height="480" viewBox="0 0 840 480">
      <rect class="orange-field" width="840" height="480" fill="var(--orange)"/>
      <circle class="white-disc" cx="140" cy="240" r="410" fill="var(--card)"/>
      <circle class="blue-arc" cx="140" cy="240" r="410" fill="none" stroke="var(--blue)" stroke-width="10"/>

      <circle cx="96" cy="180" r="26" fill="var(--blue)"/>
      <text class="brand-name" x="136" y="194" font-size="38">Talmor Ventures</text>

      <text class="service" x="70" y="290">Internet Marketing</text>
      <line x1="70" y1="312" x2="380" y2="312" stroke="var(--ink)" stroke-width="1.5"/>
      <text class="service" x="70" y="356">Web Development</text>

      <g class="icon person">
        <rect class="icon-tab" x="526" y="98" width="34" height="30"/>
        <circle class="icon-fill" cx="543" cy="108" r="5"/>
        <path class="icon-fill" d="M534 124 q9 -12 18 0 z"/>
      </g>
      <g class="icon phone">
        <rect class="icon-tab" x="534" y="138" width="34" height="30"/>
        <rect class="icon-glyph" x="545" y="142" width="12" height="22" rx="2"/>
      </g>
      <g class="icon pin">
        <rect class="icon-tab" x="540" y="178" width="34" height="30"/>
        <path class="icon-fill" d="M557 204 l-7 -11 a8 8 0 1 1 14 0 z"/>
        <circle cx="557" cy="189" r="3" fill="var(--blue)"/>
      </g>
      <g class="icon mail">
        <rect class="icon-tab" x="542" y="298" width="34" height="30"/>
        <rect class="icon-glyph" x="548" y="305" width="22" height="16"/>
        <path class="icon-glyph" d="M548 305 l11 9 l11 -9"/>
      </g>
      <g class="icon chat">
        <rect class="icon-tab" x="538" y="338" width="34" height="30"/>
        <circle class="icon-glyph" cx="555" cy="353" r="9"/>
      </g>

      <text class="contact" x="600" y="120">Mara Hollis</text>
      <text class="contact" x="600" y="160">+64 21 555 014</text>
      <text class="contact" x="600" y="200">12, Harbour Lane,</text>
      <text class="contact" x="600" y="240">Kauri House,</text>
      <text class="contact" x="600" y="280">New Zealand</text>
      <text class="contact" x="600" y="320">mara@mailbox.nz</text>
      <text class="contact" x="600" y="360">mara.talmorhq</text>
    </svg>
  </section>

  <!-- Front side: brand name -->
  <section class="card card-front" aria-label="Business card front">
    <svg width="840" height="480" viewBox="0 0 840 480">
      <rect class="orange-field" width="840" height="480" fill="var(--orange)"/>
      <circle class="white-disc" cx="180" cy="240" r="440" fill="var(--card)"/>
      <circle class="blue-arc" cx="180" cy="240" r="440" fill="none" stroke="var(--blue)" stroke-width="10"/>

      <circle cx="98" cy="240" r="26" fill="var(--blue)"/>
      <text class="brand-name" x="140" y="258" font-size="50">Talmor Ventures</text>
    </svg>
  </section>

</main>
</body>
</html>
```